今回はコーポレートサイトのTOPページのデザインをお願いしたく思います。

【素材】
素材に関しては、ロゴや写真等は現在準備中でして、
デザインの際は仮のオブジェクトを入れて対応して頂ければと思います。

【サイト構成】
サイトの構成については、ラフを書きましたので下記URLからダウンロードお願いします。
http://qvt.jp/MdRkoP

※PCを想定したデザインでお願いいたします。

【イメージ】
以下が現在の「サクラダエステート株式会社」のコーポレートサイトになります。
http://www.sakurada-estate.co.jp/

今回ご提案いただく新しいサイトのデザインは上記のものから一新して

1.スタイリッシュ
2.NY
3.最先端
4.近未来
5.エネルギッシュ
6.エキサイティング
7.自由
8.それでいてシンプル

なイメージ、従来の不動産会社のイメージに囚われないものにしたく思います。

【参考サイト】
https://www.hinamori-works.co.jp/

1ページ
グレー系
今回のデザインで採用させて頂いた方には、
コーポレートサイトの「代表メッセージ」「ニュース」「投資実績」の他3ページのデザインやコーディングなど、他のお仕事に関してもご相談させて頂ければと思います。
(もちろん当案件のみご希望の方からも募集しており、採用有無には関係ありません。)

色のコンセプトと対応の早さ、デザインの良さで決定致しました。

皆さま、お忙しい所多くのご提案を頂きまして誠にありがとうございます。
また何かございましたらお願いをさせて頂きますので引き続き宜しくお願い致します。

```html
<!DOCTYPE html>
<html lang="ja">
<head>
<meta charset="utf-8">
<title>サクラダエステート株式会社</title>
<link href="https://fonts.googleapis.com/css2?family=Montserrat:wght@400;600&family=Noto+Sans+JP:wght@400;500&family=Noto+Serif+JP:wght@400;500&display=swap" rel="stylesheet">
<style>
:root{
  --navy-deep:#141b33;
  --navy:#1e2848;
  --navy-mid:#27335a;
  --blue:#2f519c;
  --blue-light:#5577c2;
  --accent:#6f8fd6;
  --white:#ffffff;
  --text-light:#c9d1e6;
  --text-dim:#8893b3;
  --ink:#2a2f3e;
  --line:#d8dce6;
}
*{margin:0;padding:0;box-sizing:border-box}
html,body{width:1200px;height:2208px;overflow:hidden}
body{font-family:"Noto Sans JP",sans-serif;color:var(--white);background:var(--navy-deep);position:relative}
.en{font-family:"Montserrat",sans-serif;letter-spacing:.12em}
section,header,footer{position:absolute;left:0;width:1200px}

/* header */
.site-header{top:0;height:60px;background:rgba(20,27,51,.92);z-index:2}
.brand{position:absolute;left:290px;top:14px;display:flex;align-items:center;gap:8px}
.brand-mark{width:22px;height:22px;background:var(--white)}
.brand-name{font-family:"Montserrat",sans-serif;font-weight:600;font-size:22px;letter-spacing:.06em;color:var(--white)}
.brand-sub{position:absolute;left:320px;top:40px;font-size:7px;color:var(--text-light);letter-spacing:.2em}
.global-nav{position:absolute;left:590px;top:22px;display:flex;gap:38px;font-size:11px;color:var(--text-light)}

/* hero */
.hero{top:0;height:372px;background:linear-gradient(180deg,#3a4a72 0%,#2a3861 55%,#1c2647 100%)}
.hero-photo{position:absolute;inset:0;background:radial-gradient(ellipse at 50% 40%,rgba(140,160,205,.55),rgba(30,40,72,0) 65%)}
.hero-brand{position:absolute;left:480px;top:186px;display:flex;align-items:center;gap:10px}
.hero-brand .brand-mark{width:34px;height:34px}
.hero-brand .brand-name{font-size:34px}
.hero-brand-sub{position:absolute;left:526px;top:226px;font-size:9px;letter-spacing:.25em;color:var(--text-light)}
.hero-dots{position:absolute;left:560px;top:340px;display:flex;gap:8px}
.hero-dots i{width:7px;height:7px;border-radius:50%;background:var(--text-dim)}
.hero-dots i:first-child{background:var(--white)}

/* heading label */
.label{display:flex;align-items:center;gap:10px;font-size:9px;color:var(--text-dim)}
.label::before{content:"";width:40px;height:1px;background:currentColor}

/* concept */
.concept{top:372px;height:190px;background:linear-gradient(180deg,#1d2644,#232d51)}
.concept .label{position:absolute;left:290px;top:30px}
.concept-title{position:absolute;left:0;width:1200px;top:64px;text-align:center;font-family:"Noto Serif JP",serif;font-size:24px;font-weight:400;letter-spacing:.12em}
.concept-sub{position:absolute;left:0;width:1200px;top:106px;text-align:center;font-size:9px;color:var(--text-dim);letter-spacing:.2em}

/* works */
.works{top:562px;height:410px;background:var(--navy-mid)}
.works .label{position:absolute;left:290px;top:18px}
.work-num{position:absolute;top:170px;font-family:"Montserrat",sans-serif;font-size:120px;line-height:1;color:rgba(255,255,255,.06)}
.work-card{position:absolute;top:40px;width:180px;z-index:1}
.card-1{left:290px}
.card-2{left:510px}
.card-3{left:730px}
.work-photo{height:140px;background:linear-gradient(180deg,#c9d3e3,#8f9bb1)}
.work-tag{display:flex;justify-content:space-between;padding:6px 10px;background:var(--white);color:var(--ink);font-size:10px;margin:-20px 8px 0;position:relative}
.work-meta{margin-top:16px;font-size:9px;line-height:2;color:var(--text-light)}
.more-btn{position:absolute;display:flex;justify-content:space-between;align-items:center;width:120px;height:24px;padding:0 10px;border:1px solid var(--text-light);font-size:9px;color:var(--white)}
.works .more-btn{left:540px;top:368px}

/* company */
.company{top:972px;height:410px;background:linear-gradient(180deg,#2f5aae 0%,#2b4e98 60%,#223f80 100%)}
.company-photo{position:absolute;inset:0;background:linear-gradient(90deg,rgba(20,35,75,.55),rgba(20,35,75,0) 30%,rgba(20,35,75,0) 70%,rgba(20,35,75,.55))}
.company-title{position:absolute;left:0;width:1200px;top:52px;text-align:center;font-family:"Noto Serif JP",serif;font-size:20px;letter-spacing:.2em}
.company-sub{position:absolute;left:0;width:1200px;top:84px;text-align:center;font-size:8px;color:var(--text-light);letter-spacing:.2em}
.company-table{position:absolute;left:345px;top:118px;width:520px;font-size:9px;border-collapse:collapse}
.company-table th{width:78px;text-align:left;font-weight:400;padding:4px 0;color:var(--white)}
.company-table td{padding:4px 0;color:var(--text-light)}
.company-table th::before{content:"■ ";font-size:6px}
.company .more-btn{top:366px}
.company .btn-a{left:440px}.company .btn-b{left:620px}

/* news */
.news{top:1382px;height:240px;background:var(--white);color:var(--ink)}
.news .label{position:absolute;left:290px;top:26px}
.news-list{position:absolute;left:290px;top:60px;width:560px;list-style:none}
.news-item{display:flex;align-items:center;gap:16px;padding:7px 0;border-bottom:1px dotted var(--line);font-size:10px}
.news-date{width:56px;color:#667}
.news-cat{width:80px;text-align:center;background:var(--blue-light);color:var(--white);font-size:9px;padding:2px 0}

/* map */
.access-map{top:1622px;height:278px;background:linear-gradient(135deg,#e9ece4,#dde3d6 50%,#e7e9ee)}

/* footer */
.site-footer{top:1900px;height:308px;background:linear-gradient(180deg,#1a2240,#141b33)}
.footer-pattern{position:absolute;left:0;top:0;width:1200px;height:150px;background:linear-gradient(90deg,rgba(90,110,170,.25),rgba(90,110,170,0) 50%,rgba(90,110,170,.18))}
.site-footer .more-btn{left:740px;top:88px}
.footer-nav{position:absolute;left:0;width:1200px;top:148px;display:flex;justify-content:center;gap:26px;font-size:8px;color:var(--text-light)}
.footer-brand{position:absolute;left:540px;top:190px;display:flex;align-items:center;gap:8px}
.footer-brand .brand-mark{width:24px;height:24px}
.footer-brand .brand-name{font-size:22px}
.footer-address{position:absolute;left:0;width:1200px;top:238px;text-align:center;font-size:8px;color:var(--text-light)}
.copyright{position:absolute;left:0;width:1200px;top:280px;text-align:center;font-size:7px;color:var(--text-dim)}
</style>
</head>
<body>

<section class="hero">
  <div class="hero-photo" role="img" aria-label="夜の高層ビル街と並び立つビジネスパーソンのシルエット写真"></div>
  <div class="hero-brand"><span class="brand-mark"></span><span class="brand-name">SAKURADA</span></div>
  <p class="hero-brand-sub en">ESTATE · WORKS · HOME</p>
  <div class="hero-dots"><i></i><i></i><i></i></div>
</section>

<header class="site-header">
  <div class="brand"><span class="brand-mark"></span><span class="brand-name">SAKURADA</span></div>
  <p class="brand-sub en">REAL ESTATE</p>
  <nav class="global-nav en"><span>HOME</span><span>ABOUT</span><span>WORKS</span><span>NEWS</span><span>CONTACT</span></nav>
</header>

<section class="concept" role="img" aria-label="薄く重ねた都市ビル群の写真">
  <p class="label en">CONCEPT</p>
  <h2 class="concept-title">不動産の新しい未来をつくる</h2>
  <p class="concept-sub en">CREATE A NEW FUTURE OF REAL ESTATE</p>
</section>

<section class="works">
  <p class="label en">WORKS</p>
  <span class="work-num" style="left:300px">1</span>
  <span class="work-num" style="left:560px">2</span>
  <span class="work-num" style="left:800px">3</span>
  <article class="work-card card-1">
    <div class="work-photo" role="img" aria-label="白い外壁の新築住宅の写真"></div>
    <div class="work-tag"><span>不動産</span><span>（一戸建）</span></div>
    <p class="work-meta">■ 所在地：東京都世田谷区<br>■ 価格：4,980万円<br>■ 間取り：3LDK／土地120㎡<br>■ 竣工：2016年3月</p>
  </article>
  <article class="work-card card-2">
    <div class="work-photo" role="img" aria-label="二階建ての住宅の外観写真"></div>
    <div class="work-tag"><span>不動産</span><span>（一戸建）</span></div>
    <p class="work-meta">■ 所在地：神奈川県川崎市<br>■ 価格：3,680万円<br>■ 間取り：4LDK／土地110㎡<br>■ 竣工：2016年1月</p>
  </article>
  <article class="work-card card-3">
    <div class="work-photo" role="img" aria-label="白壁の二階建て住宅の外観写真"></div>
    <div class="work-tag"><span>不動産</span><span>（一戸建）</span></div>
    <p class="work-meta">■ 所在地：東京都杉並区<br>■ 価格：5,280万円<br>■ 間取り：3LDK／土地98㎡<br>■ 竣工：2015年12月</p>
  </article>
  <a class="more-btn"><span>投資実績一覧</span><span>›</span></a>
</section>

<section class="company">
  <div class="company-photo" role="img" aria-label="青空を見上げた高層ビル群と舞う葉の写真"></div>
  <h2 class="company-title">企業情報</h2>
  <p class="company-sub en">COMPANY</p>
  <table class="company-table">
    <tr><th>商号</th><td>サクラダエステート株式会社</td></tr>
    <tr><th>所在地</th><td>〒150-0000 東京都渋谷区桜丘町0-0-0 サクラダビル5F</td></tr>
    <tr><th>設立</th><td>2008年4月1日</td></tr>
    <tr><th>資本金</th><td>5,000万円</td></tr>
    <tr><th>代表者</th><td>代表取締役　桜田 湊斗</td></tr>
    <tr><th>従業員数</th><td>48名</td></tr>
    <tr><th>事業内容</th><td>不動産の売買・仲介・賃貸管理、不動産投資コンサルティング</td></tr>
    <tr><th>免許番号</th><td>国土交通大臣（0）第0000号</td></tr>
    <tr><th>所属団体</th><td>一般社団法人 桜丘住環境振興会</td></tr>
    <tr><th>取引銀行</th><td>さくら中央銀行 渋谷支店</td></tr>
  </table>
  <a class="more-btn btn-a"><span>代表メッセージ</span><span>›</span></a>
  <a class="more-btn btn-b"><span>会社概要</span><span>›</span></a>
</section>

<section class="news">
  <p class="label en">NEWS</p>
  <ul class="news-list">
    <li class="news-item"><span class="news-date">2016.05.10</span><span class="news-cat">お知らせ</span><span>新しいコーポレートサイトを公開しました。</span></li>
    <li class="news-item"><span class="news-date">2016.04.22</span><span class="news-cat">物件情報</span><span>世田谷区の新築一戸建ての販売を開始しました。</span></li>
    <li class="news-item"><span class="news-date">2016.04.08</span><span class="news-cat">お知らせ</span><span>ゴールデンウィーク期間の営業日のご案内</span></li>
    <li class="news-item"><span class="news-date">2016.03.25</span><span class="news-cat">投資実績</span><span>川崎市の収益物件の取引が完了しました。</span></li>
    <li class="news-item"><span class="news-date">2016.03.01</span><span class="news-cat">採用情報</span><span>2017年度新卒採用の募集を開始しました。</span></li>
  </ul>
</section>

<section class="access-map" role="img" aria-label="本社周辺の地図"></section>

<footer class="site-footer">
  <div class="footer-pattern" role="img" aria-label="幾何学的な三角形の装飾パターン"></div>
  <a class="more-btn"><span>アクセス</span><span>›</span></a>
  <nav class="footer-nav"><span>トップ</span><span>企業情報</span><span>代表メッセージ</span><span>投資実績</span><span>ニュース</span><span>お問い合わせ</span><span>プライバシーポリシー</span></nav>
  <div class="footer-brand"><span class="brand-mark"></span><span class="brand-name">SAKURADA</span></div>
  <p class="footer-address">〒150-0000 東京都渋谷区桜丘町0-0-0　TEL 03-0000-0000　FAX 03-0000-0001</p>
  <p class="copyright en">Copyright © SAKURADA ESTATE Co., Ltd. All Rights Reserved.</p>
</footer>

</body>
</html>
```